Concept design for a tea business Labels

Hello, we are looking for concepts for our label/packaging for a tea business that has been in business now for over a year. We are a beachy, organic, "It's your moment. Enjoy it." type tea business. We have an online website (www.corvalbrewhouse.com.au) and sell at local markets around the Tarrowby Cove area.
We are looking to upgrade our label to look more professional, in a fun/beachy/chilled out style. (unlike the traditional tea labels).
We do loose leaf tea and iced tea consentrated syrups. We have a few different packages (please see website under "sizes and packaging" bottom left). We would like to experiement with various different size and shape of labels for different products, so would like a concept design for a label using our logo (see website front page bottom). There are no colour constraints.
We use the Quillan brand labels of the following sizes:
1. Pure Glass Rectangular Product Labels, Q4825, 100/Pack, 96 x 50.8 mm
2. Pure Glass Round Multi-purpose Labels, Q3907D, 240/Pack, 40 mm diameter
3.Pure Glass Square Product Labels, Q4861, 350/Pack, 35 x 35 mm
4. For bottles we use Grained Ivory Curved Labels, Q4839, 90/Pack, 57.2 x 77 mm
If you have any more questions, please don't hesitate to contact me
Updates
Hi All,
I am considering using a box like below for packing and doing a bit of a white/beachy feel to the packaging. Either using the rectangle or round circle labels. (circle labels from quillan 60mm diameter).

Reason: Hi All - Thank you so much for all your designs. While I have seen some really beautiful designs I am excited about, it seems there was a rush at the end with a number of new designs just submitted. I still haven't seen just one design I love for the label, so I would like the opportunity to work with some of the new designers to see if we can modify to suit the concept.
Would anyone like to try a concept label with a silhouette of one of the following wave/beach/teacup? I'm just exploring a different approach as I know it is difficult tying in the beach with tea - please think - chilled out beach hut with tea/iced tea, sunrise over ocean. I like the soft colour palette - beachy feel to it - ie. Pastels - blues, greens, whites, sandy, pinks, purples, greys - sunrises over ocean, maybe a white rustic wood feel - or any other icon from Tarrowby Cove - like the Norfolk Pine's along the beach - maybe in Silhouette.
Just some more ideas.
Thank you again for all your contributions!
Petra

```html
<!DOCTYPE html>
<html lang="en">
<head>
<meta charset="utf-8">
<title>The Tarrowby Tea Company – Square Labels</title>
<link href="https://fonts.googleapis.com/css2?family=Bebas+Neue&family=Open+Sans:wght@400;600&display=swap" rel="stylesheet">
<style>
  :root {
    --stage-light: #f7f7f7;
    --stage-dark: #dcdcdc;
    --caption: #111111;
    --wave-white: #ffffff;
    --wave-silver: #cfcfcf;

    --earl-top: #dcd96a;
    --earl-mark: #b5a934;
    --earl-base: #6a9e48;
    --earl-title: #3d5a28;
    --earl-note: #3f5c2e;

    --oolong-top: #d6d4c3;
    --oolong-mark: #a09f92;
    --oolong-base: #9a8173;
    --oolong-title: #58463c;
    --oolong-note: #5e4c42;

    --breakfast-top: #cfcfd1;
    --breakfast-mark: #808082;
    --breakfast-base: #a82a36;
    --breakfast-title: #6a151d;
    --breakfast-note: #731b23;
  }
  html, body {
    margin: 0;
    width: 1200px;
    height: 1012px;
    overflow: hidden;
  }
  body {
    background: radial-gradient(ellipse 75% 70% at 50% 45%, var(--stage-light) 0%, #efefef 55%, var(--stage-dark) 100%);
    position: relative;
    font-family: "Open Sans", sans-serif;
  }
  .tea-label {
    position: absolute;
    top: 361px;
    width: 219px;
    height: 219px;
    overflow: hidden;
    box-shadow: 0 2px 5px rgba(0,0,0,0.28);
  }
  .tea-label--earl-grey { left: 164px; --top: var(--earl-top); --mark: var(--earl-mark); --base: var(--earl-base); --title: var(--earl-title); --note: var(--earl-note); }
  .tea-label--oolong { left: 427px; --top: var(--oolong-top); --mark: var(--oolong-mark); --base: var(--oolong-base); --title: var(--oolong-title); --note: var(--oolong-note); }
  .tea-label--breakfast { left: 682px; --top: var(--breakfast-top); --mark: var(--breakfast-mark); --base: var(--breakfast-base); --title: var(--breakfast-title); --note: var(--breakfast-note); }

  .tea-label__art {
    position: absolute;
    inset: 0;
    width: 219px;
    height: 219px;
  }
  .tea-label__sky { fill: var(--top); }
  .tea-label__sun { fill: var(--mark); }
  .tea-label__sea { fill: var(--base); }

  .tea-label__company {
    position: absolute;
    top: 11px;
    left: 0;
    width: 100%;
    text-align: center;
    font-size: 7px;
    font-weight: 600;
    letter-spacing: 0.2px;
    color: var(--mark);
    text-transform: uppercase;
  }
  .tea-label__name {
    position: absolute;
    top: 136px;
    left: 0;
    width: 100%;
    margin: 0;
    text-align: center;
    font-family: "Bebas Neue", sans-serif;
    font-weight: 400;
    font-size: 31px;
    line-height: 1;
    letter-spacing: -0.4px;
    color: var(--title);
  }
  .tea-label__blend {
    position: absolute;
    top: 166px;
    left: 0;
    width: 100%;
    margin: 0;
    text-align: center;
    font-size: 9.5px;
    line-height: 12px;
    color: var(--note);
  }
  .size-caption {
    position: absolute;
    left: 960px;
    top: 464px;
    width: 120px;
    text-align: center;
    font-family: Arial, Helvetica, sans-serif;
    font-size: 15px;
    line-height: 16px;
    color: var(--caption);
  }
</style>
</head>
<body>
  <svg width="0" height="0" style="position:absolute" aria-hidden="true">
    <defs>
      <linearGradient id="wave-sheen" x1="0" y1="0" x2="1" y2="1">
        <stop offset="0" stop-color="#ffffff"/>
        <stop offset="0.55" stop-color="#f4f4f4"/>
        <stop offset="1" stop-color="#c9c9c9"/>
      </linearGradient>
    </defs>
  </svg>

  <div class="tea-label tea-label--earl-grey">
    <svg class="tea-label__art" viewBox="0 0 219 219" aria-hidden="true">
      <rect class="tea-label__sky" width="219" height="219"/>
      <circle class="tea-label__sun" cx="110" cy="53" r="31"/>
      <path fill="url(#wave-sheen)" d="M0,112 C20,100 35,100 55,108 S90,116 110,106 S145,98 165,107 S200,114 219,102 V219 H0Z"/>
      <path class="tea-label__sea" d="M0,132 C20,120 35,120 55,128 S90,136 110,126 S145,118 165,127 S200,134 219,122 V219 H0Z"/>
    </svg>
    <div class="tea-label__company">The Tarrowby Tea Company</div>
    <h2 class="tea-label__name">French Earl Grey</h2>
    <p class="tea-label__blend">black tea, beromont oil,<br>peach &amp; rose petal</p>
  </div>

  <div class="tea-label tea-label--oolong">
    <svg class="tea-label__art" viewBox="0 0 219 219" aria-hidden="true">
      <rect class="tea-label__sky" width="219" height="219"/>
      <circle class="tea-label__sun" cx="110" cy="53" r="31"/>
      <path fill="url(#wave-sheen)" d="M0,112 C20,100 35,100 55,108 S90,116 110,106 S145,98 165,107 S200,114 219,102 V219 H0Z"/>
      <path class="tea-label__sea" d="M0,132 C20,120 35,120 55,128 S90,136 110,126 S145,118 165,127 S200,134 219,122 V219 H0Z"/>
    </svg>
    <div class="tea-label__company">The Tarrowby Tea Company</div>
    <h2 class="tea-label__name">Oolong Tea</h2>
    <p class="tea-label__blend">oolong green tea</p>
  </div>

  <div class="tea-label tea-label--breakfast">
    <svg class="tea-label__art" viewBox="0 0 219 219" aria-hidden="true">
      <rect class="tea-label__sky" width="219" height="219"/>
      <circle class="tea-label__sun" cx="110" cy="53" r="31"/>
      <path fill="url(#wave-sheen)" d="M0,112 C20,100 35,100 55,108 S90,116 110,106 S145,98 165,107 S200,114 219,102 V219 H0Z"/>
      <path class="tea-label__sea" d="M0,132 C20,120 35,120 55,128 S90,136 110,126 S145,118 165,127 S200,134 219,122 V219 H0Z"/>
    </svg>
    <div class="tea-label__company">The Tarrowby Tea Company</div>
    <h2 class="tea-label__name">English Breakfast</h2>
    <p class="tea-label__blend">organic black tea</p>
  </div>

  <div class="size-caption">Label<br>35mm x 35mm</div>
</body>
</html>
```